Business Card Design Project

Business card design based on the existing logo.
Updates

Target Market(s)

Small to medium business owners and CIO's looking for professional IT services.

Industry/Entity Type

Business

Font styles to use
Serif
Sans Serif

Requirements
Must have
• Logo, company name, company details

Text to appear on the business card
Name / Title:
Tom Whitlock
CEO

Address:
Veltra Limited
Level 1, 482 Korau Rd
P O Box 362
Ohakune 5918

Other details:
tom@veltra.co
Ph: 0800 519 306
Mob: +64 21 948 213
www.veltra.co

Nice to have
• I would look at both single and double sided options. My initial thought is double sided with just the logo with the grey framing for the front and the name and details on the back. But I'm open to other design options.

```html
<!DOCTYPE html>
<html lang="en">
<head>
<meta charset="utf-8">
<title>Veltra Limited – Business Card</title>
<link href="https://fonts.googleapis.com/css2?family=Arimo:wght@400;700&display=swap" rel="stylesheet">
<style>
  :root {
    --page-bg: #f9f9f9;
    --card-bg: #ffffff;
    --card-edge: #8a8a8a;
    --ink: #1a1a1a;
    --brand-blue: #1d68a0;
    --band-black: #050606;
    --logo-white: #ffffff;
  }
  html, body {
    margin: 0;
    padding: 0;
    width: 1200px;
    height: 900px;
    overflow: hidden;
    background: var(--page-bg);
    font-family: "Arimo", "Helvetica Neue", Arial, sans-serif;
  }
  .card {
    position: absolute;
    left: 68px;
    top: 136px;
    width: 1062px;
    height: 625px;
    background: var(--card-bg);
    border: 2px solid var(--card-edge);
    box-sizing: border-box;
  }
  .logo-band {
    position: absolute;
    left: 0;
    top: 375px;
    width: 646px;
    height: 174px;
    background: var(--band-black);
  }
  .logo-band__accent {
    position: absolute;
    left: 646px;
    top: 375px;
    width: 15px;
    height: 174px;
    background: var(--brand-blue);
  }
  .logo {
    position: absolute;
    left: 120px;
    top: 0;
    height: 174px;
    display: flex;
    align-items: center;
    gap: 26px;
  }
  .logo__mark {
    width: 62px;
    height: 62px;
    background: var(--brand-blue);
  }
  .logo__name {
    color: var(--logo-white);
    font-weight: 400;
    font-size: 84px;
    line-height: 1;
    letter-spacing: 0.5px;
  }
  .details {
    position: absolute;
    left: 710px;
    top: 108px;
    color: var(--ink);
    font-size: 28px;
    line-height: 36.5px;
  }
  .details p { margin: 0; }
  .person__name {
    color: var(--brand-blue);
    font-weight: 700;
    font-size: 30px;
  }
  .person__title { font-size: 30px; }
  .address { margin-top: 38px !important; }
  .contact { margin-top: 24px !important; }
</style>
</head>
<body>
  <div class="card">
    <div class="logo-band">
      <div class="logo">
        <span class="logo__mark"></span>
        <span class="logo__name">Veltra</span>
      </div>
    </div>
    <div class="logo-band__accent"></div>

    <div class="details">
      <p class="person__name">Tom Whitlock</p>
      <p class="person__title">CEO</p>
      <p class="address">Veltra Limited<br>Level 1, 482 Korau Rd<br>P O Box 362<br>Ohakune 5918</p>
      <p class="contact">tom@veltra.co<br>Ph: 0800 519 306<br>Mob: +64 21 948 213<br>www.veltra.co</p>
    </div>
  </div>
</body>
</html>
```